Robotic Physical Therapy office needs a Grand Opening Flyer

We need a Grand Opening flyer design for a robotic physical therapy office named Kestrel Motion Therapy. We would like it to have a clean, classy, upscale feeling that gives potential clients a V.I.P. feeling. We would like to use the colors black, gray, and yellow (logo will be uploaded).

Event: Thursday, June 1st, 2023 from 12pm-6pm
location: 58240 Harlan Crest Ave, Pinegate Hollow, MI 48917

Industry/Entity Type

Physical therapy

Font styles to use
Script

Colors

Designer to choose colors to be used in the design.

Requirements
Nice to have
• More of a vip feel for the invite

```html
<!DOCTYPE html>
<html lang="en">
<head>
<meta charset="UTF-8">
<title>Kestrel Motion Therapy – Grand Opening</title>
<link href="https://fonts.googleapis.com/css2?family=Montserrat:wght@500;600;700&family=Roboto:wght@900&display=swap" rel="stylesheet">
<style>
  :root {
    --yellow: #ffe500;
    --ink: #1d1d1d;
    --charcoal: #2a2a2a;
    --grey: #8e8e8e;
    --light-grey: #c9c9c9;
    --white: #ffffff;
    --sky-1: #e9f1f7;
    --sky-2: #b9cfdf;
  }
  * { margin: 0; padding: 0; box-sizing: border-box; }
  html, body { width: 848px; height: 1200px; overflow: hidden; background: var(--white); }
  .flyer {
    position: relative;
    width: 848px;
    height: 1200px;
    overflow: hidden;
    font-family: "Montserrat", sans-serif;
  }
  .backdrop {
    position: absolute; inset: 0;
    background: radial-gradient(ellipse at 40% 35%, var(--sky-1) 0%, #d3e2ec 45%, var(--sky-2) 100%);
  }
  .artwork { position: absolute; inset: 0; }
  .brand {
    position: absolute;
    top: 72px; left: 0; width: 848px;
    display: flex; justify-content: center; align-items: center; gap: 14px;
    color: var(--charcoal);
    font-weight: 700;
    font-size: 30px;
    letter-spacing: 1px;
    text-transform: uppercase;
    line-height: 1.1;
  }
  .brand-dot {
    width: 58px; height: 58px; border-radius: 50%;
    background: var(--charcoal);
    flex: none;
  }
  .brand-name span { display: block; }
  .event-title {
    position: absolute;
    top: 805px; left: 0; width: 848px;
    text-align: center;
    font-family: "Roboto", sans-serif;
    font-weight: 900;
    color: var(--yellow);
    font-size: 60px;
    line-height: 70px;
  }
  .event-date {
    position: absolute;
    top: 990px; left: 0; width: 848px;
    text-align: center;
    color: var(--white);
    font-weight: 500;
    font-size: 28px;
  }
  .event-date strong { color: var(--yellow); font-weight: 700; }
  .event-date .day { font-weight: 700; color: var(--white); }
  .event-time {
    position: absolute;
    top: 1046px; left: 0; width: 848px;
    display: flex; justify-content: center; align-items: center; gap: 20px;
    color: var(--white);
    font-weight: 600;
    font-size: 30px;
  }
  .time-pill {
    background: var(--yellow);
    color: var(--ink);
    font-size: 25px;
    font-weight: 600;
    border-radius: 20px;
    padding: 2px 26px;
    width: 202px;
    text-align: center;
  }
  .event-address {
    position: absolute;
    top: 1118px; left: 0; width: 848px;
    display: flex; justify-content: center; align-items: center; gap: 12px;
    color: var(--white);
    font-weight: 500;
    font-size: 21px;
  }
</style>
</head>
<body>
<main class="flyer">
  <div class="backdrop" role="img" aria-label="Softly blurred bright clinic corridor"></div>

  <svg class="artwork" width="848" height="1200" viewBox="0 0 848 1200" xmlns="http://www.w3.org/2000/svg">
    <defs>
      <linearGradient id="yellow-wave" x1="0" y1="0" x2="1" y2="0">
        <stop offset="0" stop-color="#ffd200"/>
        <stop offset="0.5" stop-color="#ffe500"/>
        <stop offset="1" stop-color="#fff000"/>
      </linearGradient>
      <linearGradient id="therapy-photo" x1="0" y1="0" x2="1" y2="1">
        <stop offset="0" stop-color="#f4f4f2"/>
        <stop offset="0.5" stop-color="#a9c7de"/>
        <stop offset="1" stop-color="#8a8c8e"/>
      </linearGradient>
    </defs>

    <!-- wave bands -->
    <path class="wave-grey" d="M0 602 C50 570 110 575 150 620 C185 660 215 700 270 720 L0 740 Z" fill="#7d7d7d"/>
    <path class="wave-yellow" d="M0 648 C110 655 190 718 300 728 C430 740 540 700 660 688 C740 680 800 676 848 670 L848 770 L0 770 Z" fill="url(#yellow-wave)"/>
    <path class="wave-silver" d="M560 710 C660 712 760 740 848 748 L848 760 C760 758 660 730 560 716 Z" fill="#dfe6ea"/>
    <path class="panel-dark" d="M0 668 C120 690 200 768 330 778 C460 788 560 748 670 748 C750 748 800 760 848 762 L848 1200 L0 1200 Z" fill="var(--ink)"/>
    <path class="wave-line" d="M560 722 C660 730 760 755 848 760" stroke="#f2f2f2" stroke-width="3" fill="none"/>

    <!-- framed photo -->
    <circle cx="436" cy="472" r="272" fill="var(--white)" stroke="var(--yellow)" stroke-width="10"/>
    <path d="M268 300 A240 240 0 0 0 300 690" stroke="var(--light-grey)" stroke-width="9" fill="none"/>
    <path d="M640 612 A240 240 0 0 1 360 712" stroke="var(--light-grey)" stroke-width="9" fill="none"/>
    <circle cx="440" cy="478" r="226" fill="url(#therapy-photo)" role="img" aria-label="Therapist guiding a patient through a robotic shoulder therapy device"/>
  </svg>

  <header class="brand">
    <div class="brand-dot"></div>
    <div class="brand-name"><span>Kestrel</span><span>Motion Therapy</span></div>
  </header>

  <h1 class="event-title">Robotic<br>Physical Therapy</h1>

  <p class="event-date"><span>Thursday,</span> <strong>June</strong> <span class="day">1st,</span> 2023</p>

  <p class="event-time"><span>from</span><span class="time-pill">12pm-6pm</span></p>

  <p class="event-address">
    <svg width="30" height="36" viewBox="0 0 30 36" aria-hidden="true">
      <path d="M15 2 C8 2 3 7 3 13.5 C3 21 15 31 15 31 C15 31 27 21 27 13.5 C27 7 22 2 15 2 Z" fill="var(--yellow)"/>
      <circle cx="15" cy="13.5" r="4.5" fill="var(--ink)"/>
      <ellipse cx="15" cy="32" rx="11" ry="3" fill="none" stroke="var(--yellow)" stroke-width="2.5"/>
    </svg>
    <span>58240 Harlan Crest Ave, Pinegate Hollow, MI 48917</span>
  </p>
</main>
</body>
</html>
```